Packaging design for HOT NEW RETAIL BEARD OIL BRAND - Merrow Fennick Apothecary

Packaging design for beard oils. I've attached a brief, and I've also attached a few examples of bottles and boxes. Of course, we need an entirely unique look. I've attached the photo of Merrow Fennick as well - you can choose to use it or not (I'm open).

This product will be sold at national retailers and needs to look like a brand that is sold at boutique

What the consumer wants to see on the shelf:
-Box should larger than others and be soft touch (feels luxurious)
-More “hipster look/feel”
-Text should stand out like inspiration photos - jumping off the shelf to the consumer
-Use the existing logo of Merrow Fennick
-Deco will be wrap label as shown in current product image
-Sample text to pull copy for outer carton (taken from label on glass bottle):
-Strengthen and condition your beard with this blend of natural oils. Sunflower oil is rich in omega, fatty acids and vitamins E, C, B, and A, while avocado oil hydrates the beard fibers from root to tip, keep the beard looking and feeling extraordinary. Smooth into your beard for a healthy sheen and a woodsy scent evoking the great outdoors.
-Cool/Hipster product at discount pricing

Target Market(s)

Men from ages 20-40. Women also buy this product for their men, so it needs to look like a well known brand.

Industry/Entity Type

Hair And Beauty

Font styles to use
Sans Serif

Colors

Designer to choose colors to be used in the design.

Requirements
Must have
• A full label and box design with key call outs:
• Features and benefits - found in attached brief
• Description of what it is: Beard Oil
• Name of frangrance: Sandalwood
• Size: 2 oz / 60 ml
Nice to have
• Feel free to revamp the logo if needed. I am not married to the font for Merrow Fennick Apothecary.

```html
<!DOCTYPE html>
<html lang="en">
<head>
<meta charset="utf-8">
<title>Merrow Fennick Apothecary – Men's Beard Oil Carton</title>
<link rel="stylesheet" href="https://fonts.googleapis.com/css2?family=Marcellus&family=Cutive+Mono&family=Courier+Prime:wght@400;700&family=Poppins:wght@500;700&family=Baloo+2:wght@500&display=swap">
<style>
  :root {
    --ink: #212121;
    --gold: #d5a44b;
    --white: #ffffff;
    --cut: #d31c3c;
    --fold: #27aee3;
    --art: #f4f4f4;
  }
  * { margin: 0; padding: 0; box-sizing: border-box; }
  html, body { width: 864px; height: 1200px; overflow: hidden; background: var(--ink); }
  .canvas { position: relative; width: 864px; height: 1200px; background: var(--ink); color: var(--white); }
  .dieline { position: absolute; inset: 0; }
  .dieline .cut { fill: none; stroke: var(--cut); stroke-width: 0.9; }
  .dieline .fold { fill: none; stroke: var(--fold); stroke-width: 0.9; stroke-dasharray: 3 2; }

  .abs { position: absolute; }
  .center { text-align: center; transform: translateX(-50%); white-space: nowrap; }

  .brand-name { font-family: "Marcellus", serif; letter-spacing: 0.02em; line-height: 1; }
  .brand-sub { font-family: "Cutive Mono", monospace; letter-spacing: 0.08em; line-height: 1; }

  .illustration { position: absolute; background: var(--art); border-radius: 40% 40% 45% 45%; }
  .illustration.mustache { border-radius: 50%; }

  .tagline { font-family: "Cutive Mono", monospace; font-size: 10.5px; letter-spacing: 0.06em; }
  .product-mens { font-family: "Poppins", sans-serif; font-weight: 500; color: var(--gold); line-height: 1; letter-spacing: -0.01em; }
  .product-oil { font-family: "Poppins", sans-serif; font-weight: 700; color: var(--gold); line-height: 1; letter-spacing: -0.02em; }
  .beard-types { font-family: "Courier Prime", monospace; font-weight: 700; line-height: 1; letter-spacing: 0.06em; }
  .benefits { font-family: "Cutive Mono", monospace; font-size: 11px; line-height: 14.5px; letter-spacing: 0.05em; list-style: none; }
  .scent-tag { background: var(--gold); font-family: "Baloo 2", sans-serif; font-weight: 500; color: var(--white); text-align: center; }
  .volume { font-family: "Courier Prime", monospace; font-weight: 700; font-size: 9px; letter-spacing: 0.05em; }

  .back-copy { font-family: "Courier Prime", monospace; font-size: 5.4px; line-height: 6.7px; color: #e8e8e8; width: 158px; }
  .back-copy strong { font-weight: 700; color: var(--white); }
</style>
</head>
<body>
<div class="canvas">

  <svg class="dieline" width="864" height="1200" viewBox="0 0 864 1200" aria-hidden="true">
    <!-- cut lines -->
    <path class="cut" d="M37,203.7 L43.9,196.8 L43.9,104.2 L166.6,104.2 Q170.4,104.2 171.4,108 L196.8,201 L200.5,203.7"/>
    <path class="cut" d="M200.5,203.7 L418,203.7"/>
    <path class="cut" d="M418,203.7 L421.6,200 L447,108 Q448.2,104.2 453,104.2 L574.5,104.2 L574.5,195.7 L582,203.7"/>
    <path class="cut" d="M582,203.7 L582,39.7 Q582,4.2 619,4.2 L762,4.2 Q800,4.2 800,39.7 L800,203.7"/>
    <path class="cut" d="M582,39.7 L592.5,39.7 L592.5,43.9 M800,39.7 L788,39.7 L788,43.9"/>
    <path class="cut" d="M800,203.7 L827,209 L827,526 L800,530.6"/>
    <path class="cut" d="M37,203.7 L37,530.6"/>
    <path class="cut" d="M582,530.6 L800,530.6"/>
    <path class="cut" d="M37,530.6 L40.7,534 L65,627 Q66.5,630.6 70,630.6 L193,630.6 L193,538.5 L200.5,530.6"/>
    <path class="cut" d="M200.5,530.6 L200.5,693 Q200.5,730 238,730 L381,730 Q418,730 418,693 L418,530.6"/>
    <path class="cut" d="M200.5,693 L211.6,693 L211.6,690.3 M418,693 L407.3,693 L407.3,690.3"/>
    <path class="cut" d="M418,530.6 L425.3,538.5 L425.3,630.6 L547.5,630.6 Q551,630.6 552,627 L578,534 L582,530.6"/>
    <!-- fold lines -->
    <path class="fold" d="M37,203.7 L200.5,203.7 M418,203.7 L800,203.7"/>
    <path class="fold" d="M37,530.6 L582,530.6"/>
    <path class="fold" d="M200.5,203.7 L200.5,530.6 M418,203.7 L418,530.6 M582,203.7 L582,530.6 M800,203.7 L800,530.6"/>
    <path class="fold" d="M592.5,43.9 L788,43.9"/>
    <path class="fold" d="M211.6,690.3 L407.3,690.3"/>
  </svg>

  <!-- Front panel -->
  <section class="front-panel">
    <div class="abs center brand-name" style="left:309.5px; top:223px; font-size:20px;">MERROW FENNICK</div>
    <div class="abs center brand-sub" style="left:309.5px; top:250px; font-size:13px;">APOTHECARY</div>

    <div class="illustration mustache" role="img" aria-label="White moustache illustration" style="left:228px; top:305px; width:70px; height:19px;"></div>
    <div class="illustration" role="img" aria-label="White silhouette of a bearded man's head" style="left:325px; top:280px; width:70px; height:105px;"></div>

    <div class="abs tagline" style="left:214px; top:331px;">GENTLMEN ONLY</div>
    <div class="abs product-mens" style="left:214px; top:345px; font-size:34px;">MEN’S</div>
    <div class="abs product-oil" style="left:213px; top:382px; font-size:38px;">BEARD OIL</div>
    <div class="abs beard-types" style="left:216px; top:423px; font-size:13px;">FOR ALL BEARD TYPES</div>

    <ul class="abs center benefits" style="left:309.5px; top:448px;">
      <li>• CONDITIONS DRYNESS •</li>
      <li>• SOFTENS ROUGHNESS •</li>
      <li>• COMBATS DISCOMFORT •</li>
    </ul>

    <div class="abs scent-tag" style="left:263.5px; top:495.7px; width:91.5px; height:13.5px; font-size:11px; line-height:14px;">Sandalwood</div>
    <div class="abs center volume" style="left:309.5px; top:516px;">60ml / 2 fl.oz.</div>
  </section>

  <!-- Back panel -->
  <section class="back-panel">
    <div class="abs center brand-name" style="left:500px; top:225px; font-size:7.5px;">MERROW FENNICK</div>
    <div class="abs center brand-sub" style="left:500px; top:233px; font-size:4.5px;">APOTHECARY</div>

    <div class="illustration" role="img" aria-label="White silhouette of a bearded man's head" style="left:477.7px; top:264px; width:45.5px; height:68px;"></div>

    <p class="abs back-copy" style="left:423px; top:364px;">Strengthen and condition your beard with this blend of natural oils. Sunflower oil is rich in omega, fatty acids and vitamins E, C, B, and A, while avocado oil hydrates the beard fibers from root to tip, keep the beard looking and feeling extraordinary. Smooth into your beard for a healthy sheen and a woodsy scent evoking the great outdoors.</p>
    <p class="abs back-copy" style="left:423px; top:443px;"><strong>DIRECTIONS:</strong><br>You don’t need directions– you’re a man.</p>
  </section>

  <!-- Bottle wrap label -->
  <section class="wrap-label">
    <div class="abs center brand-name" style="left:431px; top:814px; font-size:25px;">MERROW FENNICK</div>
    <div class="abs center brand-sub" style="left:431px; top:843px; font-size:13px;">APOTHECARY</div>

    <div class="illustration" role="img" aria-label="White silhouette of a bearded man's head" style="left:395px; top:872px; width:72px; height:107px;"></div>

    <div class="abs center product-mens" style="left:431px; top:983px; font-size:34px;">MEN’S</div>
    <div class="abs center product-oil" style="left:431px; top:1021px; font-size:39px;">BEARD OIL</div>
    <div class="abs center beard-types" style="left:431px; top:1063px; font-size:13px;">FOR ALL BEARD TYPES</div>
    <div class="abs center volume" style="left:431px; top:1090px;">60ml / 2 fl.oz.</div>

    <div class="abs scent-tag" style="left:0; top:1107px; width:864px; height:30.5px; font-size:16px; line-height:32px;">Sandalwood</div>
  </section>

</div>
</body>
</html>
```